qm - website template
website of specialist in neurosurgery, and teacher at the University in Milan
qm - website template - Education
Creative Brief
Education
Benedetto L. Caramuzza, MD (specialist in neurosurgery and in the history of medicine), historian and anthropologist, teaches history of medicine and health in the Faculty of Medicine, University of Velmora Castrene, where he directs the Institute for anatomical inquiry into past doctrines "(www.dulrota.it).
He's the author of over 250 papers in national and international partner to the history of medical and health disciplines and pharmacological institute of the Italian Ombrilla.
Traditional
blu (see attached logo file)
red (see attached logo file)
We need the graphic template of: • Homepage • Generic content page (text+image+ eventual document to download) • listing page of books + page with information about the selected book • listing page of conference + page with information about the selected conference • Contact The site must be optimized for 1024X768. For the main menu, it's possibile to use not system font. File must be preferably png (adobe fireworks), otherwise ai (adobe illustrator) or psd (adobe photoshop).

```html
<!DOCTYPE html>
<html lang="it">
<head>
<meta charset="utf-8">
<title>qm – Pubblicazioni scientifiche</title>
<link href="https://fonts.googleapis.com/css2?family=Ubuntu:wght@400;500;700&display=swap" rel="stylesheet">
<style>
  :root{
    --blue:#1d5e8e;
    --blue-dark:#154a72;
    --blue-link:#1f6fa8;
    --red:#9b1c22;
    --red-dark:#7e1318;
    --grey-top:#ebebeb;
    --grey-mid:#d9d9d9;
    --text:#555;
    --white:#fff;
    --placeholder:#d6d6d6;
  }
  *{box-sizing:border-box;margin:0;padding:0}
  html,body{width:1200px;height:816px;overflow:hidden}
  body{font-family:'Ubuntu',sans-serif;background:var(--grey-mid);position:relative;color:var(--text)}
  .backdrop-blue{position:absolute;left:0;top:240px;width:1200px;height:505px;background:var(--blue)}
  .backdrop-light{position:absolute;left:0;top:72px;width:1200px;height:168px;background:linear-gradient(#e4e4e4,#cfd3d6)}

  .main-nav{position:absolute;left:0;top:0;width:1200px;height:72px;background:var(--grey-top);border-bottom:1px solid #cfcfcf}
  .main-nav ul{list-style:none;display:flex;position:absolute;left:96px;top:0;height:72px;align-items:stretch}
  .main-nav li{display:flex;align-items:center;padding:0 16px;font-size:17px;color:#444}
  .main-nav li.active{background:var(--blue);color:var(--white)}

  .lang-tab{position:absolute;left:0;top:163px;width:31px;height:178px;background:var(--red);color:var(--white);
    display:flex;align-items:center;justify-content:center}
  .lang-tab span{transform:rotate(-90deg);white-space:nowrap;font-size:12px;letter-spacing:.5px}

  .page-title{position:absolute;left:96px;top:84px;width:1008px;height:132px;background:linear-gradient(90deg,var(--red-dark),var(--red) 50%,var(--red-dark));
    display:flex;align-items:center;padding-left:22px}
  .page-title h1{font-weight:400;font-size:32px;color:var(--white);letter-spacing:.5px}

  .content{position:absolute;left:96px;top:228px;width:696px;height:504px;background:var(--white);padding:0 34px 0 19px}
  .book{position:relative;height:216px;border-bottom:1px solid #ccc}
  .book:first-child{margin-top:24px}
  .book+.book{margin-top:18px;border-bottom:none;height:200px}
  .book-cover{position:absolute;left:0;top:0;width:126px;height:144px;background:var(--placeholder)}
  .book-body{position:absolute;left:142px;top:0;right:0}
  .book-body h2{font-weight:400;font-size:25px;line-height:29px;color:var(--blue-link)}
  .book-meta{font-size:11px;line-height:14px;margin-top:8px;color:#666}
  .book-text{font-size:11px;line-height:14px;margin-top:18px;color:#777}
  .read-more{position:absolute;right:0;top:170px;width:96px;height:24px;background:var(--blue);color:var(--white);
    font-size:12px;font-weight:500;display:flex;align-items:center;justify-content:center}
  .pagination{position:absolute;right:34px;top:452px;display:flex;gap:12px;font-size:16px;color:var(--blue-link);align-items:center}
  .pagination .current{background:var(--blue);color:var(--white);padding:1px 6px}

  .sidebar{position:absolute;left:804px;top:228px;width:300px;height:504px;background:var(--red);color:var(--white);padding:22px 24px 0 20px}
  .side-head{display:flex;align-items:center;gap:12px;font-size:20px;line-height:22px;margin-bottom:14px}
  .side-head svg{flex:none}
  .side-item{border-bottom:1px solid rgba(255,255,255,.35);padding:0 0 10px;margin-bottom:12px}
  .side-item h3{font-size:12px;font-weight:700}
  .side-item p{font-size:11px;line-height:14px;margin-top:3px}
  .side-group{margin-bottom:22px}
  .see-all{position:absolute;left:20px;top:440px;display:flex;align-items:center;gap:12px;font-size:20px}

  .site-footer{position:absolute;left:0;top:745px;width:1200px;height:71px;background:var(--blue-dark);color:var(--white);font-size:12px;padding:12px 0 0 108px}
  .site-footer ul{list-style:none;display:flex}
  .site-footer li+li::before{content:"|";margin:0 8px}
  .site-footer p{margin-top:10px}
  .flags{position:absolute;left:1046px;top:14px;display:flex;gap:12px}
</style>
</head>
<body>
  <div class="backdrop-light"></div>
  <div class="backdrop-blue"></div>

  <nav class="main-nav">
    <ul>
      <li>Biografia</li><li>Libri</li><li class="active">Pubblicazioni scientifiche</li><li>Conferenze</li>
      <li>Attività didattica</li><li>Attività medica</li><li>News</li><li>Link</li><li>Contatti</li>
    </ul>
  </nav>

  <div class="lang-tab"><span>SELECT YOUR LANGUAGE</span></div>

  <header class="page-title"><h1>BOOKS - CLASS APTENT TACITI SOCIOSQU AD LITORA TORQUENT</h1></header>

  <main class="content">
    <article class="book">
      <div class="book-cover" role="img" aria-label="Book cover"></div>
      <div class="book-body">
        <h2>Aliquam eu elit urna, ut fermentum augue quam dolor, aliquet vel luctus.</h2>
        <p class="book-meta">Prof. Benedetto L. Caramuzza<br>Donec porttitor, metus at sodales ultrices</p>
        <p class="book-text">Curabitur sed dolor urna. Maecenas eleifend iaculis dolor nec pharetra. Suspendisse nec ipsum odio, eu hendrerit quam. Morbi elementum ligula et elit aliquet ullamcorper in id quam.</p>
      </div>
      <span class="read-more">READ MORE</span>
    </article>
    <article class="book">
      <div class="book-cover" role="img" aria-label="Book cover"></div>
      <div class="book-body">
        <h2>Aliquam eu elit urna, ut fermentum augue quam dolor, aliquet vel luctus.</h2>
        <p class="book-meta">Prof. Benedetto L. Caramuzza<br>Donec porttitor, metus at sodales ultrices</p>
        <p class="book-text">Curabitur sed dolor urna. Maecenas eleifend iaculis dolor nec pharetra. Suspendisse nec ipsum odio, eu hendrerit quam. Morbi elementum ligula et elit aliquet ullamcorper in id quam.</p>
      </div>
      <span class="read-more">READ MORE</span>
    </article>
    <div class="pagination">
      <span>1</span><span class="current">2</span><span>3</span><span>4</span><span>5</span><span>6</span><span>7</span><span>8</span><span>|</span><span>Next</span>
    </div>
  </main>

  <aside class="sidebar">
    <div class="side-group">
      <div class="side-head">
        <svg width="22" height="26" viewBox="0 0 22 26"><rect x="1" y="1" width="20" height="24" fill="#fff"/><rect x="1" y="1" width="4" height="24" fill="#ddd"/></svg>
        <span>LIBRI</span>
      </div>
      <div class="side-item"><h3>FUSCE EU ORCI QUIS LIBERO SAGITTI</h3><p>Maecenas ac velit nec massa ultricies luctus ut non nec purus justo.</p></div>
      <div class="side-item"><h3>VIVAMUS VESTIBULUM</h3><p>Maecenas ac velit nec massa ultricies luctus ut non nec purus justo.</p></div>
    </div>
    <div class="side-group">
      <div class="side-head">
        <svg width="22" height="26" viewBox="0 0 22 26"><rect x="1" y="1" width="20" height="24" fill="#fff"/><rect x="4" y="6" width="14" height="2" fill="#bbb"/><rect x="4" y="11" width="14" height="2" fill="#bbb"/><rect x="4" y="16" width="10" height="2" fill="#bbb"/></svg>
        <span>PUBBLICAZIONI<br>SCIENTIFICHE</span>
      </div>
      <div class="side-item"><h3>DONEC SCELERISQUE JUSTO EU</h3><p>Maecenas ac velit nec massa ultricies luctus ut non nec purus justo.</p></div>
      <div class="side-item"><h3>SUSPENDISSE ALIQUET</h3><p>Maecenas ac velit nec massa ultricies luctus ut non nec purus justo.</p></div>
    </div>
    <div class="see-all">
      <svg width="22" height="22" viewBox="0 0 22 22"><rect width="22" height="22" fill="#fff"/><path d="M8 5l7 6-7 6z" fill="#9b1c22"/></svg>
      <span>SEE ALL CONFERENZE</span>
    </div>
  </aside>

  <footer class="site-footer">
    <ul>
      <li>Biografia</li><li>Libri</li><li>Pubblicazioni scientifiche</li><li>Conferenze</li><li>Attività didattica</li><li>Attività medica</li><li>News</li><li>Link</li><li>Contatti</li>
    </ul>
    <p>Prof. Benedetto L. Caramuzza © All Rights Reserved 2011.</p>
    <div class="flags">
      <svg width="18" height="12" viewBox="0 0 18 12" aria-label="Italiano"><rect width="6" height="12" fill="#2e9a4a"/><rect x="6" width="6" height="12" fill="#fff"/><rect x="12" width="6" height="12" fill="#d22630"/></svg>
      <svg width="18" height="12" viewBox="0 0 18 12" aria-label="English"><rect width="18" height="12" fill="#2b3f85"/><rect x="7" width="4" height="12" fill="#fff"/><rect y="4" width="18" height="4" fill="#fff"/><rect x="8" width="2" height="12" fill="#cf2130"/><rect y="5" width="18" height="2" fill="#cf2130"/></svg>
    </div>
  </footer>
</body>
</html>
```